Meridian Clearsound Wellness LLC Card Design

Need business card with a logo for a hearing aid sales and audiology business. We have two Hearing Instrument Specialists and one Audiologist on staff. Over 25 years in business. Locally owned and operated. Financing available. Most insurances accepted.

Meridian Clearsound Wellness LLC
48730 W Larkfield, Suite 9
Spokane, WA 99371
509-617-2084
www.meridianclearsound-example.com

Manager
Tobias Wrenfield HIS COHC
License #81957260

Target Market(s)

50yr old + people with a hearing loss.

Industry/Entity Type

Business

Contact Information for Business Card

48730 W Larkfield, Suite 9
Spokane, WA 99371
509-617-2084
www.meridianclearsound-example.com

Manager
Tobias Wrenfield HIS COHC
RTEQ #81957260

Font styles to use
Serif
Sans Serif

Requirements
Must have
• Business name, Tobias's name and title(s) and contact information, License #, web address
Nice to have
Should not have

```html
<!DOCTYPE html>
<html lang="en">
<head>
<meta charset="utf-8">
<title>Meridian Clearsound Wellness – Business Card</title>
<link rel="stylesheet" href="https://fonts.googleapis.com/css2?family=Open+Sans:wght@400;600;700&display=swap">
<style>
  :root {
    --page-bg: #ecebe8;
    --card-white: #ffffff;
    --brand-blue: #1d3f93;
    --brand-blue-deep: #184a8d;
    --ink: #2b2b2b;
    --faint: #f1f1f1;
  }
  * { margin: 0; padding: 0; box-sizing: border-box; }
  html, body {
    width: 1200px; height: 1000px; overflow: hidden;
    background: var(--page-bg);
    font-family: "Open Sans", Arial, sans-serif;
  }
  .canvas { position: relative; width: 1200px; height: 1000px; }

  .card {
    position: absolute; left: 265px; width: 665px; height: 397px;
    border-radius: 24px; overflow: hidden;
    box-shadow: 0 4px 14px rgba(0,0,0,0.18);
  }
  .card--front { top: 73px; background: var(--card-white); }
  .card--back { top: 532px; background: var(--brand-blue-deep); }

  .brand {
    position: absolute; display: flex; align-items: center; gap: 14px;
    font-weight: 600; line-height: 1.05;
  }
  .brand__dot { border-radius: 50%; flex: none; }
  .brand__name { display: block; }

  .card--front .brand { left: 32px; top: 42px; color: var(--brand-blue); font-size: 31px; }
  .card--front .brand__dot { width: 58px; height: 58px; background: var(--brand-blue); }

  .front-decor {
    position: absolute; right: -40px; top: 40px; width: 300px; height: 300px;
    border-radius: 50%; border: 26px solid var(--faint);
  }

  .company { position: absolute; left: 33px; top: 233px; font-size: 16px; color: var(--ink); line-height: 21px; }
  .company__name { color: var(--brand-blue); font-weight: 600; margin-bottom: 3px; }
  .company__name span { font-weight: 400; }
  .contact { margin-top: 14px; }
  .contact__row { display: flex; align-items: center; gap: 7px; height: 24px; }
  .contact__icon { width: 14px; height: 14px; fill: var(--brand-blue); }

  .person { position: absolute; right: 31px; top: 196px; text-align: right; color: var(--ink); font-size: 16px; line-height: 26px; }
  .person__name { color: var(--brand-blue); font-weight: 700; font-size: 20px; text-transform: uppercase; margin-bottom: 7px; }
  .person__cred { font-weight: 400; font-size: 16px; }

  .card--back .brand { left: 50%; top: 50%; transform: translate(-50%, -50%); color: #fff; font-size: 42px; white-space: nowrap; }
  .card--back .brand__dot { width: 78px; height: 78px; background: #fff; }
</style>
</head>
<body>
<main class="canvas">
  <section class="card card--front" aria-label="Business card front">
    <div class="front-decor" aria-hidden="true"></div>
    <div class="brand">
      <span class="brand__dot" aria-hidden="true"></span>
      <span class="brand__name">Meridian Clearsound<br>Wellness</span>
    </div>

    <div class="company">
      <p class="company__name">Meridian Clearsound Wellness <span>LLC</span></p>
      <p>48730 W Larkfield, Suite 9</p>
      <p>Spokane, WA 99371</p>
      <div class="contact">
        <p class="contact__row">
          <svg class="contact__icon" viewBox="0 0 16 16" aria-hidden="true"><path d="M2 6c0-2 3-4 6-4s6 2 6 4l-3 1-1-2H6L5 7 2 6zm2 2h8l1 6H3l1-6zm4 1.5a2 2 0 100 4 2 2 0 000-4z"/></svg>
          509-617-2084
        </p>
        <p class="contact__row">
          <svg class="contact__icon" viewBox="0 0 16 16" aria-hidden="true"><circle cx="8" cy="8" r="7" fill="none" stroke="currentColor" stroke-width="2" style="stroke:var(--brand-blue)"/><path d="M1 8h14M8 1c3 3 3 11 0 14M8 1c-3 3-3 11 0 14" fill="none" style="stroke:var(--brand-blue)" stroke-width="1.3"/></svg>
          www.meridianclearsound-example.com
        </p>
      </div>
    </div>

    <div class="person">
      <p class="person__name">Tobias Wrenfield <span class="person__cred">HIS COHC</span></p>
      <p>Manager</p>
      <p>License #81957260</p>
    </div>
  </section>

  <section class="card card--back" aria-label="Business card back">
    <div class="brand">
      <span class="brand__dot" aria-hidden="true"></span>
      <span class="brand__name">Meridian Clearsound<br>Wellness</span>
    </div>
  </section>
</main>
</body>
</html>
```